Flyer Design

I have a flyer made up but I prefer a more professional look
Can I just send you my logo and a copy of my current flyer that I did ....just need an exact copy
thanks
brenda

Industry/Entity Type

It Professional

```html
<!DOCTYPE html>
<html lang="en">
<head>
<meta charset="utf-8">
<title>Brenda Halloway – Session Flyer</title>
<link rel="stylesheet" href="https://fonts.googleapis.com/css2?family=Open+Sans:wght@400;700&display=swap">
<style>
  :root {
    --page-bg: #ece4d6;
    --card-bg: #ffffff;
    --purple: #9b2f86;
    --green: #a2c03c;
    --yellow: #f0cb3f;
    --sun: #f7dc6f;
    --ink: #2b2b2b;
  }
  html, body {
    margin: 0;
    padding: 0;
    width: 1200px;
    height: 1000px;
    overflow: hidden;
    background: var(--page-bg);
    font-family: "Open Sans", Arial, sans-serif;
  }
  .flyer {
    position: absolute;
    left: 280px;
    top: 50px;
    width: 640px;
    height: 900px;
    background: var(--card-bg);
    box-shadow: 0 6px 18px rgba(0,0,0,0.25);
    display: flex;
    flex-direction: column;
  }
  .brand {
    height: 258px;
    display: flex;
    align-items: center;
    justify-content: center;
    gap: 22px;
  }
  .brand-mark {
    width: 74px;
    height: 74px;
    border-radius: 50%;
    background: var(--sun);
    flex: none;
  }
  .brand-name {
    color: var(--purple);
    font-size: 50px;
    font-weight: 400;
    letter-spacing: 0.5px;
    margin: 0;
  }
  .band {
    height: 72px;
    display: flex;
    align-items: center;
    justify-content: center;
    color: #fff;
    font-weight: 700;
    font-size: 27px;
    letter-spacing: 1.5px;
    text-transform: uppercase;
    margin: 0;
  }
  .band--prices { background: var(--purple); }
  .band--booking { background: var(--green); }
  .band--location { background: var(--yellow); }
  .details {
    display: flex;
    flex-direction: column;
    justify-content: center;
    align-items: center;
    text-align: center;
    color: var(--ink);
    font-size: 22px;
    line-height: 1.42;
    margin: 0;
  }
  .details--prices { height: 109px; }
  .details--booking { height: 143px; }
  .details--location { height: 176px; }
  .details p { margin: 0; }
</style>
</head>
<body>
  <article class="flyer">
    <header class="brand">
      <span class="brand-mark"></span>
      <h1 class="brand-name">Brenda Halloway</h1>
    </header>

    <h2 class="band band--prices">Session Prices</h2>
    <section class="details details--prices">
      <p>Single 60 minute session: $140 + $14 gst = $154</p>
      <p>Package of five sessions: $650 + $65 gst = $715</p>
    </section>

    <h2 class="band band--booking">Book a Session</h2>
    <section class="details details--booking">
      <p>Via the website at: www.brendahalloway.com</p>
      <p>Via email at: bhalloway@fastmail.net.au</p>
      <p>Via mobile/SMS on: 0412 555 208</p>
    </section>

    <h2 class="band band--location">Location</h2>
    <section class="details details--location">
      <p>Ground floor, 72 Harbourview Road,</p>
      <p>Westcliff, NSW 2031</p>
      <p>(Opposite Westcliff train station, with two hour</p>
      <p>free parking in the Westcliff shopping centre)</p>
    </section>
  </article>
</body>
</html>
```